Flyer to promote new Commercial HVAC Preventative Maintenance clients

This flyer will be in the body of emails that will be sent to new, existing, and/or potential commericial buildings HVAC clients. It will have the least amount of words used, but it will convey the point with pertinent pictorial and graphics. It will show the value of a Periodic/Preventative routine maintenance to lower operating costs of their commericial buildings (i.e. office, medical, shopping centers, apartment, warehouse facility, etc.), in the following ways:
1) Reduce monthly power usage,
2) Reduce emergency HVAC service calls,
3) Reduce costly repairs costs,
4) Reduce HVAC down-times and angry tenants,
5) Increases the life expectancy of the existing and/or new HVAC equipment in the building and/or the equipment's' early replacement costs,
6) Reduces tenant's early termination of their lease and law suits against the landlords,
7) Increases tenant's renewal of the lease and agree to pay the increase rental rates,
8) Reduces unhappy customers and increases tenant's productivity,
9) By reducing the landlord's expenses, the value of the property will increase considerably and profitable to sell their holdings, or refinance and keep their holdings with an increased ROI (Return On Investment).

Landlords can not depend on their tenants' obligation to maintain the landlords' major assets, which is their HVAC equipment and systems.

With the periodic maintenance done by one reliable and licensed HVAC company, the will not use different companies that may or may not do the right repair job on their unit and hurt their bottom line and increase HVAC replacement COSTLY rates.

```html
<!DOCTYPE html>
<html lang="en">
<head>
<meta charset="utf-8">
<title>Professional HVAC Maintenance</title>
<link href="https://fonts.googleapis.com/css2?family=Oswald:wght@700&family=Montserrat:wght@500&family=Rubik:wght@500&family=Open+Sans:wght@400;700;800&display=swap" rel="stylesheet">
<style>
  :root {
    --blue-deep: #0b4f94;
    --blue-mid: #1467b3;
    --cyan: #14d2f5;
    --navy: #0d3f7a;
    --ink: #1c1c28;
    --paper: #f2f3f5;
    --rule: #d9dce1;
    --white: #ffffff;
    --black: #111111;
  }
  * { margin: 0; padding: 0; box-sizing: border-box; }
  html, body { width: 1200px; height: 2602px; overflow: hidden; }
  body { background: var(--paper); position: relative; font-family: "Open Sans", sans-serif; }

  .hero {
    position: absolute; left: 0; top: 0; width: 1200px; height: 543px;
    background: linear-gradient(100deg, var(--blue-deep) 0%, var(--blue-mid) 55%, #3c8fd0 100%);
    border-bottom-left-radius: 95px;
    overflow: hidden;
  }
  .hero-photo {
    position: absolute; left: 622px; top: 0; width: 578px; height: 543px;
    background: linear-gradient(180deg, #8fc0e6 0%, #cfe3f2 45%, #b8bcc2 70%, #7d838b 100%);
    border-bottom-left-radius: 40px;
  }
  .hero-title {
    position: absolute; left: 75px; top: 66px;
    font-family: "Oswald", sans-serif; font-weight: 700;
    color: var(--white); font-size: 86px; line-height: 1; letter-spacing: -1px;
  }
  .hero-subtitle {
    position: absolute; left: 75px; top: 170px; width: 515px;
    border-top: 3px solid var(--white); border-bottom: 3px solid var(--white);
    font-family: "Oswald", sans-serif; font-weight: 700;
    color: var(--cyan); font-size: 64px; line-height: 86px; letter-spacing: -0.5px;
    white-space: nowrap;
  }
  .hero-tagline {
    position: absolute; left: 75px; top: 292px;
    font-family: "Montserrat", sans-serif; font-weight: 500;
    color: var(--white); font-size: 48px; line-height: 60px;
  }

  .benefit-icon { position: absolute; left: 75px; width: 112px; height: 112px; }
  .benefit-text {
    position: absolute; left: 248px; width: 860px;
    font-family: "Rubik", sans-serif; font-weight: 500;
    color: var(--ink); font-size: 28px; line-height: 37.5px;
  }
  .benefit-text.single { white-space: nowrap; width: auto; }
  .rule { position: absolute; left: 248px; width: 877px; height: 2px; background: var(--rule); }

  .note {
    position: absolute; left: 145px; width: 910px; text-align: center;
    font-size: 21px; line-height: 31px; color: var(--ink);
  }

  .contact-band {
    position: absolute; left: 0; top: 2188px; width: 1200px; height: 243px;
    background: linear-gradient(90deg, #0f55a0 0%, #1a6fbf 50%, #0f55a0 100%);
  }
  .web-pill {
    position: absolute; left: 132px; top: 2152px; width: 942px; height: 94px;
    background: var(--cyan); border: 4px solid var(--white); border-radius: 47px;
    text-align: center; font-weight: 800; font-size: 56px; line-height: 86px; color: var(--black);
  }
  .phone {
    position: absolute; left: 0; top: 2272px; width: 1200px; text-align: center;
    font-weight: 800; font-size: 108px; line-height: 120px; color: var(--white);
  }
  .phone svg { vertical-align: -10px; margin-right: 26px; }
  .footer {
    position: absolute; left: 0; top: 2431px; width: 1200px; height: 171px; background: var(--black);
  }
  .footer-line {
    position: absolute; left: 0; width: 1200px; text-align: center;
    font-weight: 700; font-size: 45px; line-height: 56px; color: var(--white);
  }
  .footer-line svg { vertical-align: -4px; margin-right: 16px; }
</style>
</head>
<body>
<svg width="0" height="0" style="position:absolute">
  <defs>
    <symbol id="ring" viewBox="0 0 112 112">
      <circle cx="56" cy="56" r="48" fill="#fff" stroke="#0d3f7a" stroke-width="6"/>
      <path d="M6 52 A50 50 0 0 1 86 12" fill="none" stroke="#14d2f5" stroke-width="7" stroke-linecap="round"/>
    </symbol>
  </defs>
</svg>

<header class="hero">
  <div class="hero-photo" role="img" aria-label="Technician in blue overalls servicing a rooftop HVAC condenser unit with an open red tool case"></div>
  <div class="hero-title">PROFESSIONAL</div>
  <div class="hero-subtitle">HVAC MAINTENANCE</div>
  <div class="hero-tagline">Protect Your Assets,<br>Ensure Efficiency, &amp;<br>Control Costs.</div>
</header>

<section class="benefit-list">
  <svg class="benefit-icon" style="top:596px" viewBox="0 0 112 112"><use href="#ring"/><g fill="none" stroke="#0d3f7a" stroke-width="5" stroke-linejoin="round" stroke-linecap="round"><path d="M60 26 L46 50 L62 50 L50 70"/><path d="M56 66 V86 M46 76 L56 86 L66 76"/></g></svg>
  <div class="benefit-text single" style="top:634px">Reduce monthly power usage</div>
  <div class="rule" style="top:718px"></div>

  <svg class="benefit-icon" style="top:730px" viewBox="0 0 112 112"><use href="#ring"/><g fill="none" stroke="#0d3f7a" stroke-width="5" stroke-linejoin="round" stroke-linecap="round"><path d="M34 40 C30 62 48 82 70 80 L76 70 L64 62 L58 68 C50 64 46 58 44 52 L50 46 L44 34 Z"/><path d="M58 42 A10 10 0 0 1 78 42 V50 H58 Z"/></g></svg>
  <div class="benefit-text single" style="top:768px">Reduce emergency HVAC service calls</div>
  <div class="rule" style="top:853px"></div>

  <svg class="benefit-icon" style="top:860px" viewBox="0 0 112 112"><use href="#ring"/><g fill="none" stroke="#0d3f7a" stroke-width="6" stroke-linecap="round"><path d="M36 36 L76 76 M76 36 L36 76"/><circle cx="56" cy="56" r="9" fill="#fff" stroke-width="4"/></g></svg>
  <div class="benefit-text single" style="top:898px">Reduce costly repairs costs</div>
  <div class="rule" style="top:984px"></div>

  <svg class="benefit-icon" style="top:995px" viewBox="0 0 112 112"><use href="#ring"/><g fill="none" stroke="#0d3f7a" stroke-width="5"><circle cx="56" cy="58" r="20"/><circle cx="56" cy="58" r="5" fill="#0d3f7a"/><path d="M56 53 C50 44 58 40 62 44 M60 60 C68 62 68 70 62 70 M52 61 C46 66 42 60 45 56"/><circle cx="78" cy="80" r="6" fill="#0d3f7a" stroke="none"/></g></svg>
  <div class="benefit-text single" style="top:1033px">Reduce HVAC down-times and angry tenants</div>
  <div class="rule" style="top:1118px"></div>

  <svg class="benefit-icon" style="top:1139px" viewBox="0 0 112 112"><use href="#ring"/><g fill="none" stroke="#0d3f7a" stroke-width="5" stroke-linejoin="round"><path d="M56 28 L62 34 L72 32 L74 42 L82 48 L78 58 L82 68 L72 72 L68 82 L58 78 L50 84 L44 76 L34 74 L36 64 L30 56 L36 48 L34 38 L44 36 L50 28 Z"/><circle cx="56" cy="56" r="12"/></g></svg>
  <div class="benefit-text" style="top:1138px">Increases the life expectancy of the existing and/or new HVAC<br>equipment in the building and/or the equipment's' early<br>replacement costs</div>
  <div class="rule" style="top:1268px"></div>

  <svg class="benefit-icon" style="top:1276px" viewBox="0 0 112 112"><use href="#ring"/><g fill="none" stroke="#0d3f7a" stroke-width="5" stroke-linejoin="round"><circle cx="46" cy="42" r="10"/><path d="M28 76 C28 62 36 56 46 56 C52 56 56 58 58 62"/><path d="M58 74 L72 62 L86 74 M62 72 V84 H82 V72" fill="#0d3f7a"/></g></svg>
  <div class="benefit-text" style="top:1294px">Reduces tenant's early termination of their lease and law suits<br>against the landlords</div>
  <div class="rule" style="top:1400px"></div>

  <svg class="benefit-icon" style="top:1412px" viewBox="0 0 112 112"><use href="#ring"/><g fill="none" stroke="#0d3f7a" stroke-width="5" stroke-linejoin="round" stroke-linecap="round"><path d="M34 62 L48 48 L58 56 L76 36 M66 36 H76 V46"/><path d="M28 78 H48 C54 78 58 74 64 72 L80 66 M28 84 H54"/></g></svg>
  <div class="benefit-text" style="top:1426px">Increases tenant's renewal of the lease and agree to pay the<br>increase rental rates</div>
  <div class="rule" style="top:1537px"></div>

  <svg class="benefit-icon" style="top:1549px" viewBox="0 0 112 112"><use href="#ring"/><g fill="none" stroke="#0d3f7a" stroke-width="5" stroke-linejoin="round" stroke-linecap="round"><circle cx="56" cy="56" r="24" stroke-dasharray="8 5" stroke-width="8"/><path d="M44 64 L52 56 L58 60 L68 48 M62 48 H68 V54"/></g></svg>
  <div class="benefit-text single" style="top:1576px">Reduces unhappy customers and increases tenant's productivity</div>
  <div class="rule" style="top:1659px"></div>

  <svg class="benefit-icon" style="top:1684px" viewBox="0 0 112 112"><use href="#ring"/><g fill="none" stroke="#0d3f7a" stroke-width="5" stroke-linejoin="round" stroke-linecap="round"><path d="M32 62 L56 42 L80 62 M38 58 V84 H74 V58"/><path d="M46 38 V24 M40 30 L46 24 L52 30 M66 38 V24 M60 30 L66 24 L72 30"/><text x="56" y="79" font-family="Rubik, sans-serif" font-size="20" fill="#0d3f7a" stroke="none" text-anchor="middle">$</text></g></svg>
  <div class="benefit-text" style="top:1683px">By reducing the landlord's expenses, the value of the property<br>will increase considerably and profitable to sell their holdings,<br>or refinance and keep their holdings with an increased ROI<br>(Return On Investment).</div>
</section>

<p class="note" style="top:1905px">Landlords can not depend on their tenants' obligation to maintain the landlords' major assets, which is their HVAC equipment and systems.</p>
<p class="note" style="top:1998px">With the periodic maintenance done by one reliable and licensed HVAC company, the will not use different companies that may or may not do the right repair job on their unit and hurt their bottom line and increase HVAC replacement COSTLY rates.</p>

<div class="contact-band"></div>
<div class="web-pill">www.northbreezehvac.com</div>
<div class="phone"><svg width="104" height="96" viewBox="0 0 104 96"><g fill="none" stroke="#fff" stroke-width="8" stroke-linecap="round"><path d="M18 14 C6 40 34 82 70 86 L80 70 L62 58 L54 66 C42 60 34 50 30 40 L38 32 L30 12 Z" fill="#fff"/><path d="M60 30 A14 14 0 0 1 72 42 M62 14 A30 30 0 0 1 88 40"/></g></svg>(555) 014-2871</div>

<footer class="footer">
  <div class="footer-line" style="top:27px"><svg width="40" height="40" viewBox="0 0 40 40"><circle cx="20" cy="20" r="19" fill="#14d2f5"/><rect x="9" y="12" width="22" height="16" rx="2" fill="#111"/><path d="M10 14 L20 22 L30 14" fill="none" stroke="#14d2f5" stroke-width="2.5"/></svg>Service@northbreezehvacteam.com</div>
  <div class="footer-line" style="top:88px"><svg width="38" height="44" viewBox="0 0 38 44"><path d="M19 2 C9 2 2 9 2 18 C2 30 19 42 19 42 C19 42 36 30 36 18 C36 9 29 2 19 2 Z" fill="#14d2f5"/><circle cx="19" cy="18" r="7" fill="#111"/></svg>4821 Juniper Ave #210 Henderson, NV 89012</div>
</footer>
</body>
</html>
```